Bramblewick Systems Group - IT Services Company/Managed Services/Consulting Card Design

Our company needs a business card design that will appeal to client companies with 50-1000 employees. We do IT services, administration, management, projects, budgeting and consulting (Like a small Corvatel.com, Plumvary.com or Tundrabox.com). Mainly helping businesses use technology to be more competitive and efficient. We work with IT Infrastructure, switches, routers, firewalls and Cloud, Verlanta/Linux servers, Quellon server virtualization, Datacenter environments, Email systems, Business Systems, Backup, Disaster Recovery, Data Security, NVX, Deskora 12 and Halcyte.) Would like the final design to be professional but stand out to our prospective clients. Our current logo is attached. Color or design could be changed. Overall looking for a great finished product, original ideas are welcome and would pay more for the right one. If you think you have a better logo idea include a general idea if you can. Web design has not been done yet so that is a later possibility too.

Target Market(s)

1st - Mid-sized companies with 100-1000 employees with technology needs
2nd - Smaller companies with 20-99 employees with technology needs
- These companies can be in many different industries. Heathcare, legal, manufacturing, education, non-profit, services

Industry/Entity Type

Information Technology

Contact Information for Business Card

Should include the following info:

Logo or other logo with Company Name

Martin J. Cosgrove

Principal

BramblewickSys.com

mcosgrove@BramblewickSys.com

(866) 7-BRAMBLE x 348

Font styles to use
Other font styles liked:
• designer can decide

Requirements
Must have
• Professional, appealing design, appeal to the target market
Nice to have
• Some sort of additional accent design that would stand out could be nice. I thought of adding a graphic in the top left corner that would look like the corner of the card was becoming more and more pixelated as it got near the corner, with some pixels missing.

```html
<!DOCTYPE html>
<html lang="en">
<head>
<meta charset="utf-8">
<title>Bramblewick Systems Group – Business Card</title>
<link rel="stylesheet" href="https://fonts.googleapis.com/css2?family=Crimson+Text:wght@400;600;700&display=swap">
<style>
  :root {
    --page-bg: #e4e2de;
    --card-bg: #f7f6f3;
    --ink: #1d1d3a;
    --navy: #24245a;
    --navy-deep: #181845;
    --tagline: #2e4a9a;
    --muted: #3a3a4a;
    --accent: #c98c88;
  }
  * { box-sizing: border-box; margin: 0; padding: 0; }
  html, body {
    width: 1200px; height: 970px; overflow: hidden;
    background: var(--page-bg);
    font-family: "Crimson Text", Georgia, serif;
  }
  .card {
    position: absolute; left: 100px; top: 184px;
    width: 1000px; height: 602px;
    background: var(--card-bg);
    box-shadow: 0 10px 30px rgba(0,0,0,.15);
    overflow: hidden;
  }
  .brand {
    position: absolute; left: 0; right: 0; top: 52px;
    text-align: center; color: var(--ink);
    font-weight: 600; line-height: 1;
  }
  .brand-name { font-size: 56px; letter-spacing: 1px; }
  .brand-sub { font-size: 22px; letter-spacing: 5px; text-transform: uppercase; margin-top: 6px; }
  .tagline {
    position: absolute; left: 0; right: 0; top: 140px;
    text-align: center; color: var(--tagline);
    font-size: 21px; letter-spacing: 2px; text-transform: uppercase;
    line-height: 1;
  }
  .tagline-rule {
    position: absolute; left: 305px; width: 390px; top: 170px;
    height: 2px; background: var(--tagline);
  }
  .person {
    position: absolute; right: 587px; top: 262px; text-align: right;
  }
  .person-name { font-size: 33px; font-weight: 700; color: #3a3f5c; line-height: 1.1; white-space: nowrap; }
  .person-role { font-size: 24px; color: var(--muted); margin-top: 4px; }
  .divider {
    position: absolute; left: 475px; top: 228px;
    width: 4px; height: 148px; background: var(--navy);
  }
  .contact { position: absolute; left: 522px; top: 228px; list-style: none; }
  .contact li {
    display: flex; align-items: center; gap: 12px;
    height: 40px; margin-bottom: 10px;
    font-size: 24px; color: var(--ink); white-space: nowrap;
  }
  .contact svg { width: 40px; height: 40px; flex: none; }
  .rules { position: absolute; left: 0; right: 0; top: 438px; }
  .rules span { display: block; height: 4px; background: var(--navy); margin-bottom: 6px; }
  .band {
    position: absolute; left: 0; right: 0; top: 458px; bottom: 0;
    background: linear-gradient(180deg, var(--navy) 0%, var(--navy-deep) 100%);
    display: flex; flex-direction: column; align-items: center; justify-content: center; gap: 18px;
  }
  .services { display: flex; gap: 28px; list-style: none; }
  .services li {
    display: flex; align-items: center; gap: 8px;
    font-size: 27px; color: var(--accent);
  }
  .services svg { width: 26px; height: 26px; }
</style>
</head>
<body>
<main class="card">
  <div class="brand">
    <div class="brand-name">Bramblewick</div>
    <div class="brand-sub">Systems Group</div>
  </div>
  <p class="tagline">Reliable. Secure. Efficient.</p>
  <div class="tagline-rule"></div>

  <div class="person">
    <p class="person-name">Martin J. Cosgrove</p>
    <p class="person-role">Principal</p>
  </div>
  <div class="divider"></div>

  <ul class="contact">
    <li>
      <svg viewBox="0 0 40 40"><circle cx="20" cy="20" r="19" fill="#1d1d3a"/><path d="M14 11c1-1 2-1 3 0l2 3c.6 1 .4 2-.4 2.6l-1.2 1c1 2.4 2.7 4.1 5 5l1-1.2c.6-.8 1.6-1 2.6-.4l3 2c1 1 1 2 0 3l-1.5 1.5c-5 1-14-8-13-13z" fill="#fff"/></svg>
      (866) 7-BRAMBLE x 348
    </li>
    <li>
      <svg viewBox="0 0 40 40"><circle cx="20" cy="20" r="19" fill="#1d1d3a"/><rect x="10" y="13" width="20" height="14" fill="none" stroke="#fff" stroke-width="2"/><path d="M10 13l10 8 10-8" fill="none" stroke="#fff" stroke-width="2"/></svg>
      mcosgrove@BramblewickSys.com
    </li>
    <li>
      <svg viewBox="0 0 40 40"><circle cx="20" cy="20" r="19" fill="#1d1d3a"/><g fill="none" stroke="#fff" stroke-width="2.4" stroke-linecap="round"><path d="M18 16l3-3a4 4 0 0 1 6 6l-3 3"/><path d="M22 24l-3 3a4 4 0 0 1-6-6l3-3"/><path d="M17 23l6-6"/></g></svg>
      www.BramblewickSys.com
    </li>
  </ul>

  <div class="rules"><span></span><span></span></div>

  <section class="band">
    <ul class="services">
      <li><svg viewBox="0 0 26 26"><circle cx="13" cy="13" r="12" fill="#c98c88"/><path d="M7.5 13.5l4 4 7-8" fill="none" stroke="#24245a" stroke-width="2.6"/></svg>IT services</li>
      <li><svg viewBox="0 0 26 26"><circle cx="13" cy="13" r="12" fill="#c98c88"/><path d="M7.5 13.5l4 4 7-8" fill="none" stroke="#24245a" stroke-width="2.6"/></svg>Administration</li>
      <li><svg viewBox="0 0 26 26"><circle cx="13" cy="13" r="12" fill="#c98c88"/><path d="M7.5 13.5l4 4 7-8" fill="none" stroke="#24245a" stroke-width="2.6"/></svg>Management</li>
    </ul>
    <ul class="services">
      <li><svg viewBox="0 0 26 26"><circle cx="13" cy="13" r="12" fill="#c98c88"/><path d="M7.5 13.5l4 4 7-8" fill="none" stroke="#24245a" stroke-width="2.6"/></svg>Projects</li>
      <li><svg viewBox="0 0 26 26"><circle cx="13" cy="13" r="12" fill="#c98c88"/><path d="M7.5 13.5l4 4 7-8" fill="none" stroke="#24245a" stroke-width="2.6"/></svg>Budgeting</li>
      <li><svg viewBox="0 0 26 26"><circle cx="13" cy="13" r="12" fill="#c98c88"/><path d="M7.5 13.5l4 4 7-8" fill="none" stroke="#24245a" stroke-width="2.6"/></svg>Consulting</li>
    </ul>
  </section>
</main>
</body>
</html>
```